Album cover design for spiritual/ceremony artist

Marla Tevrin is a talented singer-songwriter who produces music for plant medicine, Breathwork, and healing ceremonies. Her musical style is a divine feminine flow of folk and indie that carries a heart healing message.

She is looking for analbum cover for her next release.

1 - We want the background to be a mandala very similar to the one I am sharing. We would like to use these same type colors and design

2 - She would like to have an image of a sufi dancer over the top of a the mandala. We ONLY WANT the silhouette of the dancer, kind of like the one shown in the brief.

3 - the text should be very simple - Just her name - “Marla Tevrin” - and the title of the album which is “The Ember”

Font styles to use
Script

Colors
EE7325
F08F49
F5BC92
FAE3D3
FDF4ED
EB3D1F
EC4F4E
F09395
F8D3D4
FCEDEE
E54698
E96AAD
F1A4CE
F9D9EA
FCEFF6
A7469A
B969AE
D3A5CF
EDDBEB
F8F0F9

Requirements
Must have
• Mandala in the background as shown in the brief, and a silhouette Sufi dancer woman over the top of it

```html
<!DOCTYPE html>
<html lang="en">
<head>
<meta charset="utf-8">
<title>Marla Tevrin — The Ember</title>
<link rel="stylesheet" href="https://fonts.googleapis.com/css2?family=Sacramento&family=Montserrat:wght@500&display=swap">
<style>
  :root {
    --night: #10173a;
    --night-deep: #0c1230;
    --violet: #4a2a8a;
    --plum: #8a2f8f;
    --magenta: #c8336e;
    --ember-red: #eb3d1f;
    --ember-orange: #ee7325;
    --ember-glow: #f5bc92;
    --ember-core: #fae3d3;
    --ink-light: #fdf4ed;
  }
  * { margin: 0; padding: 0; box-sizing: border-box; }
  html, body {
    width: 1200px;
    height: 1200px;
    overflow: hidden;
    background: var(--night-deep);
  }
  .album-cover {
    position: relative;
    width: 1200px;
    height: 1200px;
    overflow: hidden;
    background: linear-gradient(180deg, #1a1f4a 0%, var(--night) 70%, var(--night-deep) 100%);
  }
  .cover-artwork {
    position: absolute;
    inset: 0;
    width: 1200px;
    height: 1200px;
    display: block;
  }
  .cover-titles {
    position: absolute;
    left: 0;
    right: 0;
    top: 940px;
    text-align: center;
    color: var(--ink-light);
  }
  .artist-name {
    font-family: "Sacramento", cursive;
    font-weight: 400;
    font-size: 96px;
    line-height: 1;
    letter-spacing: 1px;
  }
  .album-title {
    margin-top: 38px;
    font-family: "Montserrat", sans-serif;
    font-weight: 500;
    font-size: 40px;
    letter-spacing: 5px;
    text-transform: uppercase;
    line-height: 1;
  }
</style>
</head>
<body>
  <main class="album-cover">
    <svg class="cover-artwork" viewBox="0 0 1200 1200" xmlns="http://www.w3.org/2000/svg">
      <defs>
        <radialGradient id="haze-gradient" cx="600" cy="460" r="640" gradientUnits="userSpaceOnUse">
          <stop offset="0" stop-color="#5a2a86" stop-opacity="0.9"/>
          <stop offset="0.7" stop-color="#3a2470" stop-opacity="0.6"/>
          <stop offset="1" stop-color="#1a1f4a" stop-opacity="0"/>
        </radialGradient>
        <radialGradient id="mandala-gradient" cx="600" cy="470" r="510" gradientUnits="userSpaceOnUse">
          <stop offset="0" stop-color="#fae3d3"/>
          <stop offset="0.3" stop-color="#f5bc92"/>
          <stop offset="0.55" stop-color="#ee7325"/>
          <stop offset="0.75" stop-color="#eb3d1f"/>
          <stop offset="0.9" stop-color="#c8336e"/>
          <stop offset="1" stop-color="#8a2f8f"/>
        </radialGradient>
        <linearGradient id="floor-gradient" x1="0" y1="0" x2="0" y2="1">
          <stop offset="0" stop-color="#1c1d4c"/>
          <stop offset="1" stop-color="#10173a"/>
        </linearGradient>
        <clipPath id="above-floor">
          <rect x="0" y="0" width="1200" height="893"/>
        </clipPath>
      </defs>
      <g clip-path="url(#above-floor)">
        <rect class="purple-haze" x="0" y="0" width="1200" height="893" fill="url(#haze-gradient)"/>
        <circle class="mandala-dancer-art" cx="600" cy="465" r="507" fill="url(#mandala-gradient)"
                role="img" aria-label="Glowing orange and magenta mandala with the silhouette of a Sufi dancer twirling in a flared skirt, arms outstretched"/>
      </g>
      <rect class="stage-floor" x="0" y="893" width="1200" height="307" fill="url(#floor-gradient)"/>
    </svg>
    <header class="cover-titles">
      <h1 class="artist-name">Marla Tevrin</h1>
      <h2 class="album-title">The Ember</h2>
    </header>
  </main>
</body>
</html>
```